Casa and Valor Website Re-design

Already Wordpress base. Needs to be updated and better presentation. Current site: www.valorcasa.example redirected from www.casaandvalors.example
Site purpose is to offer information and get leads from potential heroes looking to buy, rent or sell a home
Here is a link to the video to be used as well: https://www.videohost.example/watch?v=Lm8RtPz3VwK

I own the video and logo
The video spells out the program. We will need a page for REALTORS to sign up, a page for our Vendors and their benefits
Steadfast Lending, Marpen Odari offers a reduced rate plus they will pay the upfront cost of the $600 VA appraisal
Hero Buyers get 25% rebate after escrow
Hero Sellers get 25% off a normal 6% Listing
Copperfield Inspections will give a 10% off discount for heroes
Also need a page for the Medic Gives program

Direct competitor: www.nestsforvalor.example

Target Market(s)

veterans, teachers, government employees, nurses, 1st responders

Industry/Entity Type

Realtor

Coding

Coded - Design and coding required

Number of Pages Required

5+ page

Colors
ec1f27
ffffff
3176b5

Requirements
Must have
• clean and correct throughout, ability to collect leads with FB login, or names and phone and email information. Colors are Navy Blue, Burgandy Red, and White
Nice to have
• photos

```html
<!DOCTYPE html>
<html lang="en">
<head>
<meta charset="utf-8">
<title>Casa &amp; Valor</title>
<link rel="stylesheet" href="https://fonts.googleapis.com/css2?family=Montserrat:wght@400;600;700;800&family=Open+Sans:ital,wght@0,400;0,600;0,700;1,400&display=swap">
<style>
:root{
  --red:#ec1f27;
  --blue:#3176b5;
  --navy:#1f3f73;
  --white:#ffffff;
  --ink:#3b3f47;
  --muted:#8a8f98;
  --light:#f1f2f4;
  --footer-left:#3c3f46;
  --footer-right:#33363c;
}
*{box-sizing:border-box;margin:0;padding:0}
html,body{width:1200px;height:2396px;overflow:hidden;background:var(--white)}
body{font-family:"Open Sans",Arial,sans-serif;color:var(--ink);position:relative}
h1,h2,h3{font-family:"Montserrat",Arial,sans-serif}

/* header */
.site-header{position:absolute;top:0;left:0;width:1200px;height:84px;background:var(--white);display:flex;align-items:center;padding:0 40px;z-index:3}
.brand{display:flex;align-items:center;gap:10px;font-family:"Montserrat",sans-serif;font-weight:800;font-size:22px;color:var(--navy)}
.brand-dot{width:14px;height:14px;border-radius:50%;background:var(--red)}
.main-nav{margin-left:auto;display:flex;align-items:center;gap:30px;font-family:"Montserrat",sans-serif;font-size:13px;font-weight:600;color:var(--ink)}
.main-nav .active{color:var(--blue)}
.nav-phone{display:flex;align-items:center;gap:8px;color:var(--blue)}
.btn{display:inline-block;font-family:"Montserrat",sans-serif;font-weight:700;font-size:14px;color:var(--white);border-radius:3px;padding:12px 26px}
.btn-red{background:var(--red)}
.btn-blue{background:var(--blue)}

/* hero */
.hero-photo{position:absolute;top:84px;left:0;width:1200px;height:396px;background:linear-gradient(120deg,#2b3850 0%,#4f6584 40%,#8b9bb2 70%,#3a4763 100%)}
.hero-form{position:absolute;top:300px;left:268px;width:664px;height:210px;background:var(--blue);text-align:center;padding-top:30px;color:var(--white);z-index:2;box-shadow:0 10px 30px rgba(0,0,0,.2)}
.hero-form h1{font-size:30px;font-weight:800}
.hero-form p{font-size:15px;margin-top:6px;opacity:.9}
.hero-fields{display:flex;gap:14px;justify-content:center;margin-top:22px}
.field{background:var(--white);color:var(--muted);font-size:13px;height:36px;width:250px;text-align:left;padding:9px 14px;display:flex;justify-content:space-between}
.hero-form .btn{margin-top:16px;padding:10px 36px}

/* intro */
.intro{position:absolute;top:540px;left:0;width:1200px;height:380px;overflow:hidden}
.intro-text{position:absolute;left:150px;top:40px;width:560px}
.intro-text h2{font-size:40px;font-weight:800;color:var(--blue)}
.rule{width:60px;height:4px;background:var(--red);margin:14px 0 18px}
.intro-text p{font-size:14px;line-height:1.7;color:var(--muted);margin-bottom:12px}
.intro-text .btn{margin-top:8px}
.intro-emblem{position:absolute;left:800px;top:20px;width:460px;height:460px;border-radius:50%;background:linear-gradient(135deg,#2b558f,#1f3f73)}

/* savings band */
.savings{position:absolute;top:920px;left:0;width:1200px;height:400px;background:var(--blue)}
.video-card{position:absolute;left:160px;top:60px;width:380px;height:300px;background:var(--white);padding:10px;box-shadow:0 10px 24px rgba(0,0,0,.25)}
.video-art{width:360px;height:236px;background:linear-gradient(160deg,#5aa7de,#2d6fb0)}
.video-caption{display:flex;align-items:center;gap:10px;padding-top:12px;font-family:"Montserrat",sans-serif;font-weight:700;color:var(--navy);font-size:16px}
.play{width:26px;height:26px;border-radius:50%;background:var(--red);display:flex;align-items:center;justify-content:center}
.savings-text{position:absolute;left:620px;top:90px;width:440px;color:var(--white)}
.savings-text h3{font-size:22px;font-weight:600}
.savings-text h2{font-size:32px;font-weight:800;margin-top:4px}
.savings-text p{font-size:14px;line-height:1.6;margin:18px 0 24px;opacity:.92}

/* offers */
.offers{position:absolute;top:1340px;left:0;width:1200px;height:220px;background:var(--light);display:flex;gap:60px;padding:54px 0 0 160px}
.offer{width:300px}
.offer-num{font-family:"Montserrat",sans-serif;font-size:38px;font-weight:700;color:#c9ccd2}
.offer p{font-size:16px;line-height:1.5;color:var(--ink);margin-top:6px}
.offer strong{color:var(--red);font-weight:700}

/* testimonial */
.testimonial{position:absolute;top:1580px;left:0;width:1200px;height:380px;text-align:center}
.quote-mark{margin:34px auto 0;width:40px;height:34px}
.testimonial blockquote{width:820px;margin:24px auto 0;font-size:16px;line-height:1.7;color:var(--muted)}
.avatars{display:flex;justify-content:center;align-items:center;gap:22px;margin-top:34px}
.avatar{border-radius:50%;background:linear-gradient(135deg,#b7bcc4,#6f7580)}
.avatar.small{width:56px;height:56px;opacity:.7}
.avatar.large{width:78px;height:78px;border:4px solid var(--white);box-shadow:0 0 0 2px var(--blue)}
.author{font-family:"Montserrat",sans-serif;font-weight:700;font-size:14px;color:var(--ink);margin-top:14px;letter-spacing:1px}
.author-role{font-size:12px;color:var(--muted);margin-top:2px}

/* footer */
.site-footer{position:absolute;top:1960px;left:0;width:1200px;height:436px;display:flex}
.footer-info{width:540px;background:var(--footer-left);color:#c8ccd3;padding:50px 0 0 40px;font-size:14px}
.footer-info h3{color:var(--white);font-size:20px;font-weight:700;margin-bottom:26px}
.footer-label{display:flex;align-items:center;gap:8px;font-size:13px;color:#9ea3ab}
.footer-value{color:var(--white);margin:4px 0 16px;line-height:1.5}
.socials{display:flex;gap:10px;margin:8px 0 24px}
.socials span{width:28px;height:28px;border-radius:50%;background:#5c616a}
.copyright{font-size:12px;color:#9ea3ab;line-height:1.5}
.footer-form{flex:1;background:var(--footer-right);padding:50px 60px 0;position:relative;color:var(--white)}
.footer-form h3{font-size:18px;font-weight:600;margin-bottom:22px}
.input{width:420px;height:40px;background:#8e939b;color:#d8dbe0;font-size:13px;padding:11px 14px;margin-bottom:12px}
.input.tall{height:120px}
.send{position:absolute;left:462px;top:340px;width:42px;height:42px;border-radius:50%;background:var(--white);display:flex;align-items:center;justify-content:center}
.to-top{position:absolute;right:60px;top:40px}
</style>
</head>
<body>

<header class="site-header">
  <div class="brand"><span class="brand-dot"></span>Casa &amp; Valor</div>
  <nav class="main-nav">
    <span class="active">HOME</span>
    <span>HOW IT WORKS</span>
    <span>HERO ADVANTAGES</span>
    <span>CONTACT US</span>
    <span class="nav-phone">
      <svg width="14" height="14" viewBox="0 0 24 24"><path fill="#3176b5" d="M6.6 10.8a15 15 0 0 0 6.6 6.6l2.2-2.2c.3-.3.7-.4 1-.2 1.1.4 2.3.6 3.6.6.6 0 1 .4 1 1V20c0 .6-.4 1-1 1A17 17 0 0 1 3 4c0-.6.4-1 1-1h3.5c.6 0 1 .4 1 1 0 1.3.2 2.5.6 3.6.1.3 0 .7-.2 1z"/></svg>
      (555) 010-4663
    </span>
    <span class="btn btn-red">Sign Up</span>
  </nav>
</header>

<div class="hero-photo" role="img" aria-label="Photo of uniformed police officers smiling together"></div>

<section class="hero-form">
  <h1>Are you a hometown hero?</h1>
  <p>Connect with a local specialist today to maximize your savings</p>
  <div class="hero-fields">
    <div class="field">Name</div>
    <div class="field">I am interested in <span>&#9662;</span></div>
  </div>
  <span class="btn btn-red">Continue &rarr;</span>
</section>

<section class="intro">
  <div class="intro-text">
    <h2>Casa &amp; Valor</h2>
    <div class="rule"></div>
    <p>Our mission is to provide extraordinary savings to heroes who provide selfless service to our nation and the communities where they live and work every day.</p>
    <p>Casa &amp; Valor is a growing network of local real estate agents, lenders and service partners committed to giving back to heroes. Since our start we have helped teachers, nurses, veterans and first responders save thousands on buying, selling or renting a home. It is our way to say thank you.</p>
    <span class="btn btn-blue">Discover More</span>
  </div>
  <div class="intro-emblem" role="img" aria-label="Large decorative star emblem"></div>
</section>

<section class="savings">
  <div class="video-card">
    <div class="video-art" role="img" aria-label="Video still announcing great news for local heroes"></div>
    <div class="video-caption">
      <span class="play"><svg width="10" height="12" viewBox="0 0 10 12"><path fill="#fff" d="M0 0l10 6-10 6z"/></svg></span>
      How It Works?
    </div>
  </div>
  <div class="savings-text">
    <h3>How to Save with</h3>
    <h2>Casa &amp; Valor?</h2>
    <p>Steadfast Lending offers a reduced rate plus they will pay the upfront cost of the $600 VA appraisal.</p>
    <span class="btn btn-red">Sign Up</span>
  </div>
</section>

<section class="offers">
  <div class="offer"><div class="offer-num">01.</div><p>Hero Buyers get <strong>25% rebate</strong> after escrow</p></div>
  <div class="offer"><div class="offer-num">02.</div><p>Hero Sellers get <strong>25% off</strong> a normal 6% Listing</p></div>
  <div class="offer"><div class="offer-num">03.</div><p>Copperfield Inspections will give a <strong>10% off discount</strong> for heroes</p></div>
</section>

<section class="testimonial">
  <svg class="quote-mark" viewBox="0 0 40 34"><path fill="#3176b5" d="M0 34V18C0 8 6 2 16 0l2 4c-6 2-9 6-9 12h8v18zm22 0V18c0-10 6-16 16-18l2 4c-6 2-9 6-9 12h8v18z"/></svg>
  <blockquote>"I was very excited to find this. As a teacher, money is tight. Lorem ipsum has been the industry's standard dummy text ever. The additional money I received allowed me to buy a bedroom set for my daughter's room."</blockquote>
  <div class="avatars">
    <span class="avatar small" role="img" aria-label="Customer portrait"></span>
    <span class="avatar large" role="img" aria-label="Portrait of Dorian Vale"></span>
    <span class="avatar small" role="img" aria-label="Customer portrait"></span>
  </div>
  <div class="author">DORIAN VALE</div>
  <div class="author-role">Teacher</div>
</section>

<footer class="site-footer">
  <div class="footer-info">
    <h3>Casa &amp; Valor</h3>
    <div class="footer-label"><svg width="12" height="12" viewBox="0 0 24 24"><path fill="#9ea3ab" d="M6.6 10.8a15 15 0 0 0 6.6 6.6l2.2-2.2c.3-.3.7-.4 1-.2 1.1.4 2.3.6 3.6.6.6 0 1 .4 1 1V20c0 .6-.4 1-1 1A17 17 0 0 1 3 4c0-.6.4-1 1-1h3.5c.6 0 1 .4 1 1 0 1.3.2 2.5.6 3.6.1.3 0 .7-.2 1z"/></svg>Call us</div>
    <div class="footer-value">(555) 010-4663</div>
    <div class="footer-label"><svg width="12" height="12" viewBox="0 0 24 24"><path fill="#9ea3ab" d="M12 2a7 7 0 0 0-7 7c0 5 7 13 7 13s7-8 7-13a7 7 0 0 0-7-7zm0 9.5A2.5 2.5 0 1 1 12 6.5a2.5 2.5 0 0 1 0 5z"/></svg>Location</div>
    <div class="footer-value">1420 Orchard Lane,<br>Springdale NV 89000</div>
    <div class="footer-label">Follow Us</div>
    <div class="socials"><span></span><span></span><span></span></div>
    <div class="copyright">&copy; 2017 Casa &amp; Valor<br>All Rights Reserved</div>
  </div>
  <div class="footer-form">
    <h3>Drop Us a Message</h3>
    <div class="input">Name</div>
    <div class="input">Email</div>
    <div class="input">Call #</div>
    <div class="input tall">Message</div>
    <span class="send"><svg width="18" height="18" viewBox="0 0 24 24"><path fill="#33363c" d="M2 21l21-9L2 3v7l15 2-15 2z"/></svg></span>
    <svg class="to-top" width="20" height="26" viewBox="0 0 20 26"><path fill="none" stroke="#fff" stroke-width="2" d="M10 26V2M2 10l8-8 8 8"/></svg>
  </div>
</footer>

</body>
</html>
```